We need a .psd design for a store we are creating called Bright Pouches. I will need only the main home page designed.

The store will be an eCommerce website that sells custom printed men's wallets. Customers will come onto the website and be able to upload their own images or add text to the front, back and inside of the wallet. We will initially be launching with one wallet style and will be expanding our range in the future for now the only images of a wallet on the website should be of the style attached.

There will be multiple templates that a customer can choose and edit the design of so there will effectively be a large number of products on display in the store. However, on the homepage there should just be a couple of featured products and the main emphasis should be on the features of the wallet/website and links to other areas of the website (customise your own wallet, edit our templates, bespoke designer wallets).

For the styling of the website, it needs to be funky and fresh with lots of colour. The logo of the website is attached and the styling should mirror the logo style.

The main features of the website should be on the home page. These features are:
- 5 year money back guarantee on wallet
- High quality, durable leather, made to last
- customer can upload photo and edit them online with our online picture editor
- 3d mockup of the wallet as you are designing it to show what it looks like with custom images on
- Edit any of our ready made wallet designs

Features of this wallet may be used as well - these can be viewed on "Image 6" of the attached product image .psd files.

Attached are the logo for the website and the wallet product photos. The product photos are provided in .psd format and have smart objects so that you can add any image to the front/inside of the wallets for any images on the website you create. Fee free to edit them and use them for banner images and feature images however you feel necessary.

The term "what does you wallet say about you" should be used as this is a tagline for most of the marketing - based on the fact that the wallets are personalised to each individual they will show off that individuals personality and what they like.

The eventual website will be hosted on cartnest and will more than likely use the "StallKit" theme. This is a highly adaptable theme and examples of the layout styles for the homepage can be found here: http://reef.lindolayouts.example/cartnest/stallkit-intro/?storefront=pixora-assets however i do not want you to just copy a ready made template and stick some stock photos in - I only want one page designing here, put the effort in with the banners and feature images and you'll win this.

Any images that you create for hero sliders/banners should be provided in .psd format so that they can be edited as necessary in the future. A newsletter popup should also be designed as the website will have postwren integration, the newsletter popup is a 500 x 750 image that pops up with a message saying "subscribe to our newsletter and get 10% off your next order".

There should also be an area of the page that has customer testimonials.

Target Market(s)

Males, aged 18 - 45

Industry/Entity Type

Retail

Number of Pages Required

1 page

Font styles to use
Serif
Decorative
Script

Colors

Designer to choose colors to be used in the design.

Requirements
Must have
• Vibrant and uplifting feel to the website
• Design which reflects the logo
• Features of the website and wallets should feature prominently on the homepage (but not in banner/hero image)
Nice to have
• hipster/geek/easygoing vibe
• Images that have used the wallet .psd files and have different designs on them showing customers that anything can be printed on the wallets
• Custom images/styles for the featured images and main banner.
Should not have
• - Boring images
• - Stock Photos
• - Mundane feel
• - Square block style images - try putting images in circles or geometric shapes with colours, just adding a stock photo to some "lorem Ipsum" text will not win you this contest

```html
<!DOCTYPE html>
<html lang="en">
<head>
<meta charset="utf-8">
<title>Bright Pouches — Home</title>
<link rel="stylesheet" href="https://fonts.googleapis.com/css2?family=Bebas+Neue&family=Oswald:wght@400;500&family=Roboto:wght@400&display=swap">
<style>
  :root {
    --stage: #e6e6e6;
    --red: #c00000;
    --red-text: #e53935;
    --yellow: #f2c300;
    --green: #00ad6a;
    --white: #ffffff;
    --ink: #222222;
    --steel: #555555;
    --grey-photo: #b9b9b9;
    --grey-crowd: #9a9a9a;
    --blue: #1e9be0;
    --splash-red: #ec4a3c;
    --splash-blue: #7fd0e3;
  }
  html, body { margin: 0; padding: 0; }
  body {
    width: 1200px; height: 1200px; overflow: hidden;
    background: var(--stage); position: relative;
  }
  .page-source { position: absolute; width: 0; height: 0; overflow: hidden; }
  .homepage { position: absolute; top: 19px; width: 390px; height: 1162px; display: block; }
  .homepage--left { left: 107px; }
  .homepage--right { left: 702px; }
  .display { font-family: "Bebas Neue", "Oswald", sans-serif; }
  .body-cond { font-family: "Oswald", "Arial Narrow", sans-serif; }
  .ui { font-family: "Roboto", Arial, sans-serif; }
  .nav-link { fill: var(--red-text); font-size: 14px; }
  .hero-title { fill: var(--red-text); font-size: 33px; letter-spacing: .5px; }
  .section-title { fill: var(--white); font-size: 38px; }
  .step-title { fill: var(--steel); font-size: 30px; }
  .step-copy { fill: var(--white); font-size: 11.5px; }
  .feature-item { fill: var(--yellow); font-size: 22px; }
  .contact-title { fill: var(--ink); font-size: 25px; }
  .field-label { fill: var(--ink); font-size: 10px; }
  .pay-name { fill: var(--red); font-size: 14px; }
  .foot-head { fill: #444; font-size: 4.5px; }
  .foot-link { fill: #555; font-size: 4.2px; }
  .cut-line { stroke: var(--white); stroke-width: 1; stroke-dasharray: 5 3; fill: none; }
  .step-icon { fill: none; stroke: #777; stroke-width: 2; }
</style>
</head>
<body>

<svg class="page-source" xmlns="http://www.w3.org/2000/svg" aria-hidden="true">
  <defs>
    <linearGradient id="splash-tone" x1="0" y1="0" x2="1" y2="1">
      <stop offset="0" stop-color="var(--splash-red)" stop-opacity="0.55"/>
      <stop offset="1" stop-color="var(--splash-blue)" stop-opacity="0.55"/>
    </linearGradient>
  </defs>
  <symbol id="homepage" viewBox="0 0 488 1452">
    <rect width="488" height="1452" fill="var(--white)"/>

    <!-- header -->
    <circle cx="40" cy="45" r="24" fill="var(--green)"/>
    <text class="display" x="72" y="44" font-size="19" fill="var(--ink)">Bright</text>
    <text class="display" x="72" y="61" font-size="19" fill="var(--ink)">Pouches</text>
    <text class="display nav-link" x="157" y="42">Guide</text>
    <text class="display nav-link" x="193" y="42">Templates</text>
    <text class="display nav-link" x="258" y="42">Image editor</text>
    <text class="display nav-link" x="332" y="42">Contacts</text>
    <rect x="401" y="26" width="19" height="19" rx="3" fill="#bdbdbd"/>
    <rect x="427" y="26" width="19" height="19" rx="3" fill="#bdbdbd"/>
    <rect x="453" y="26" width="19" height="19" rx="3" fill="var(--blue)"/>

    <!-- hero -->
    <rect role="img" aria-label="Grey studio backdrop behind the wallet" x="0" y="82" width="488" height="248" fill="var(--grey-photo)"/>
    <polygon points="0,330 488,218 488,330" fill="var(--red)"/>
    <rect role="img" aria-label="Black printed wallet with custom artwork" x="18" y="112" width="198" height="180" rx="8" fill="#1b1b1b"/>
    <rect role="img" aria-label="Open and closed wallet product shots" x="248" y="212" width="216" height="62" rx="4" fill="#262626"/>
    <circle cx="53" cy="127" r="42" fill="var(--blue)"/>
    <circle cx="53" cy="127" r="37" fill="var(--red)"/>
    <text class="display" x="20" y="134" font-size="46" fill="var(--yellow)">5</text>
    <text class="display" x="52" y="108" font-size="12" fill="var(--white)">Year</text>
    <text class="display" x="52" y="120" font-size="12" fill="var(--white)">Money</text>
    <text class="display" x="52" y="132" font-size="12" fill="var(--white)">Back</text>
    <text class="display" x="21" y="149" font-size="14" fill="var(--white)">Guarantee</text>
    <text class="display hero-title" x="474" y="109" text-anchor="end">Get your custom</text>
    <text class="display hero-title" x="474" y="146" text-anchor="end">wallets in 3 steps!</text>
    <circle cx="210" cy="302" r="3" fill="none" stroke="var(--white)" stroke-width="1.2"/>
    <circle cx="225" cy="302" r="3" fill="var(--white)"/>
    <circle cx="240" cy="302" r="3" fill="var(--white)"/>
    <circle cx="254" cy="302" r="3" fill="var(--white)"/>
    <circle cx="268" cy="302" r="3" fill="var(--white)"/>

    <!-- how to -->
    <polygon points="0,330 488,330 488,446 0,354" fill="var(--red)"/>
    <line class="cut-line" x1="0" y1="321" x2="488" y2="321"/>
    <text class="display section-title" x="237" y="367" text-anchor="middle">How to</text>
    <polygon points="0,354 488,446 488,666 0,666" fill="var(--yellow)"/>
    <polygon points="0,580 488,660 488,666 0,666" fill="var(--green)"/>
    <rect role="img" aria-label="Paint splash artwork in red, blue and green" x="328" y="466" width="160" height="196" fill="url(#splash-tone)"/>

    <circle cx="116" cy="428" r="41" fill="var(--white)" stroke="var(--yellow)" stroke-width="2"/>
    <rect class="step-icon" x="101" y="413" width="30" height="30" rx="3"/>
    <polyline points="104,440 114,428 121,435 128,426 128,440" fill="#888"/>
    <circle cx="116" cy="520" r="41" fill="var(--white)" stroke="var(--yellow)" stroke-width="2"/>
    <rect class="step-icon" x="93" y="503" width="46" height="34" rx="5"/>
    <circle cx="116" cy="610" r="41" fill="var(--white)" stroke="var(--yellow)" stroke-width="2"/>
    <polygon points="98,600 116,590 134,600" fill="#777"/>
    <rect class="step-icon" x="100" y="602" width="32" height="18"/>

    <text class="display step-title" x="188" y="418">Step 1</text>
    <text class="body-cond step-copy" x="189" y="437">Upload Your image or use one of our</text>
    <text class="body-cond step-copy" x="189" y="454">templates and edit the image with</text>
    <text class="body-cond step-copy" x="189" y="471">our on-line picture editor</text>
    <text class="display step-title" x="188" y="516">Step 2</text>
    <text class="body-cond step-copy" x="189" y="534">Get 3D view of Your wallets</text>
    <text class="display step-title" x="188" y="607">Step 3</text>
    <text class="body-cond step-copy" x="189" y="625">Make Your order</text>
    <line class="cut-line" x1="0" y1="665" x2="488" y2="665"/>

    <!-- features -->
    <polygon points="0,666 488,666 488,714 0,820" fill="var(--green)"/>
    <polygon points="0,820 488,714 488,856 0,961" fill="var(--white)"/>
    <text class="display section-title" x="245" y="715" text-anchor="middle">Features</text>
    <circle cx="403" cy="712" r="14" fill="none" stroke="var(--white)" stroke-width="6" stroke-dasharray="4 3"/>
    <circle cx="435" cy="693" r="9" fill="none" stroke="var(--white)" stroke-width="5" stroke-dasharray="3 2"/>
    <circle cx="114" cy="806" r="82" fill="var(--white)" stroke="#dcdcdc" stroke-width="3"/>
    <circle role="img" aria-label="Printed wallet beside its colourful gift box" cx="114" cy="806" r="76" fill="var(--splash-blue)"/>
    <text class="display feature-item" x="216" y="797">High quality</text>
    <text class="display feature-item" x="216" y="823">Durable leather</text>
    <text class="display feature-item" x="216" y="849">Made to last</text>
    <text class="display feature-item" x="216" y="875">Gift box</text>

    <!-- we accept -->
    <polygon points="0,961 488,856 488,1146 0,1021" fill="var(--red)"/>
    <line class="cut-line" x1="130" y1="936" x2="488" y2="936"/>
    <text class="display section-title" x="249" y="978" text-anchor="middle">We accept</text>
    <g class="display pay-name" text-anchor="middle">
      <rect x="56" y="996" width="42" height="28" rx="2" fill="var(--white)"/><text x="77" y="1015">Orvo</text>
      <rect x="121" y="996" width="42" height="28" rx="2" fill="var(--white)"/><text x="142" y="1015">Penta</text>
      <rect x="186" y="996" width="42" height="28" rx="2" fill="var(--white)"/><text x="207" y="1015">Lumen</text>
      <rect x="251" y="996" width="42" height="28" rx="2" fill="var(--white)"/><text x="272" y="1015">Quell</text>
      <rect x="316" y="996" width="42" height="28" rx="2" fill="var(--white)"/><text x="337" y="1015">Tally</text>
      <rect x="381" y="996" width="42" height="28" rx="2" fill="var(--white)"/><text x="402" y="1015">Ferro</text>
    </g>

    <!-- contact -->
    <polygon role="img" aria-label="Group of young men in casual clothing, faded grey" points="0,1021 488,1146 488,1260 0,1221" fill="var(--grey-crowd)"/>
    <text class="display contact-title" x="29" y="1074">Have a question?</text>
    <text class="display contact-title" x="29" y="1103">Contact us</text>
    <text class="ui field-label" x="31" y="1123">Your name:</text>
    <rect x="30" y="1128" width="196" height="24" rx="3" fill="var(--white)"/>
    <text class="ui field-label" x="31" y="1181">Your e-mail:</text>
    <rect x="30" y="1186" width="196" height="24" rx="3" fill="var(--white)"/>
    <polygon role="img" aria-label="Yellow doodle pattern" points="0,1221 488,1260 488,1286 0,1351" fill="var(--yellow)"/>
    <rect x="30" y="1234" width="70" height="20" rx="3" fill="var(--white)"/>
    <text class="ui" x="65" y="1248" font-size="11" text-anchor="middle" fill="var(--red)">SUBMIT</text>

    <!-- footer -->
    <circle cx="111" cy="1380" r="24" fill="var(--green)"/>
    <text class="ui foot-head" x="161" y="1371">RECENT NEWS</text>
    <text class="ui foot-link" x="161" y="1385">About us</text>
    <text class="ui foot-link" x="161" y="1392">Services</text>
    <text class="ui foot-link" x="161" y="1399">Selected Work</text>
    <text class="ui foot-link" x="161" y="1406">Get In Touch</text>
    <text class="ui foot-link" x="161" y="1413">Careers</text>
    <text class="ui foot-head" x="245" y="1371">CATEGORIES</text>
    <text class="ui foot-link" x="245" y="1385">Business</text>
    <text class="ui foot-link" x="245" y="1392">Design</text>
    <text class="ui foot-link" x="245" y="1399">Real life</text>
    <text class="ui foot-link" x="245" y="1406">Science</text>
    <text class="ui foot-link" x="245" y="1413">Tech</text>
    <text class="ui foot-head" x="329" y="1371">SUBSCRIBE</text>
    <text class="ui foot-link" x="329" y="1385">Get monthly updates and free resources.</text>
    <rect x="333" y="1396" width="50" height="11" rx="5.5" fill="#f1f1f1"/>
    <text class="ui foot-link" x="358" y="1403" text-anchor="middle">Email</text>
    <rect x="386" y="1396" width="41" height="11" rx="5.5" fill="var(--blue)"/>
    <text class="ui foot-link" x="406" y="1403" text-anchor="middle" fill="var(--white)">Subscribe</text>
    <text class="ui foot-link" x="105" y="1439">© Copyright 2017 Bright Pouches - All Rights Reserved</text>
  </symbol>
</svg>

<svg class="homepage homepage--left" viewBox="0 0 488 1452" xmlns="http://www.w3.org/2000/svg" aria-label="Bright Pouches home page">
  <use href="#homepage" width="488" height="1452"/>
</svg>

<svg class="homepage homepage--right" viewBox="0 0 488 1452" xmlns="http://www.w3.org/2000/svg" aria-label="Bright Pouches home page">
  <use href="#homepage" width="488" height="1452"/>
</svg>

</body>
</html>
```